business cards

we want our logos on the back
the information on it are on the design I've uploaded
come up with whatever you think is best, we want something professional, sophisticated and sleek.

```html
<!DOCTYPE html>
<html lang="en">
<head>
<meta charset="utf-8">
<title>Kestrel Physio Studio — Business Cards</title>
<link rel="stylesheet" href="https://fonts.googleapis.com/css2?family=Montserrat:wght@300;400;600&display=swap">
<style>
  :root {
    --page: #c9ced4;
    --page-light: #e3e6ea;
    --card: #232323;
    --card-deep: #1b1b1b;
    --green: #4cb848;
    --white: #f2f2f2;
    --muted: #d8d8d8;
    --pill: #e9e9e9;
  }
  * { box-sizing: border-box; margin: 0; padding: 0; }
  html, body { width: 1200px; height: 675px; overflow: hidden; }
  body {
    font-family: "Montserrat", sans-serif;
    background: radial-gradient(ellipse at 45% 60%, var(--page-light), var(--page));
    display: flex;
    align-items: center;
    justify-content: center;
    gap: 48px;
  }
  .card {
    width: 520px;
    height: 318px;
    background: linear-gradient(160deg, var(--card), var(--card-deep));
    border-radius: 4px;
    box-shadow: 0 14px 30px rgba(0,0,0,0.28);
    position: relative;
    overflow: hidden;
    color: var(--white);
  }

  /* Back of card */
  .card-back {
    display: flex;
    flex-direction: column;
    align-items: center;
    padding-top: 98px;
  }
  .brand-name {
    font-weight: 300;
    font-size: 30px;
    letter-spacing: 1px;
    color: var(--white);
    line-height: 1.2;
  }
  .appointment {
    margin-top: 34px;
    width: 380px;
    display: grid;
    grid-template-columns: auto 1fr auto 1fr;
    align-items: center;
    column-gap: 6px;
    row-gap: 10px;
    font-size: 12px;
  }
  .field-pill {
    height: 14px;
    border-radius: 7px;
    background: var(--pill);
  }
  .field-pill.wide { grid-column: 1 / -1; }
  .social-row {
    display: flex;
    gap: 8px;
    margin-top: 22px;
  }
  .social-dot {
    width: 18px;
    height: 18px;
    border-radius: 50%;
    background: var(--green);
  }

  /* Front of card */
  .card-front { padding: 44px 0 0 44px; }
  .person-name {
    font-weight: 600;
    font-size: 22px;
    line-height: 1.2;
    color: var(--green);
    margin-bottom: 6px;
  }
  .credentials {
    list-style: none;
    font-size: 11.5px;
    line-height: 1.45;
    color: var(--muted);
  }
  .credentials .role { text-transform: uppercase; }
  .contact-list {
    list-style: none;
    position: absolute;
    left: 58px;
    bottom: 36px;
    font-size: 12.5px;
    line-height: 1.55;
    color: var(--muted);
  }
  .contact-list li { display: flex; align-items: center; gap: 8px; }
  .contact-list svg { width: 12px; height: 12px; fill: var(--green); flex: none; }
</style>
</head>
<body>

  <section class="card card-back" aria-label="Card back">
    <div class="brand-name">Kestrel Physio Studio</div>
    <div class="appointment">
      <span>Date:</span><span class="field-pill"></span>
      <span>Time:</span><span class="field-pill"></span>
      <span class="field-pill wide"></span>
    </div>
    <div class="social-row">
      <span class="social-dot"></span>
      <span class="social-dot"></span>
      <span class="social-dot"></span>
    </div>
  </section>

  <section class="card card-front" aria-label="Card front">
    <h1 class="person-name">Daniel Maroudis</h1>
    <ul class="credentials">
      <li class="role">Director</li>
      <li class="role">Senior Physiotherapist</li>
      <li>BAppSc, MPhysio, GradCert Sports Rehab</li>
      <li>Accredited Strength Coach</li>
    </ul>

    <ul class="contact-list">
      <li>
        <svg viewBox="0 0 24 24"><path d="M6.6 10.8a15 15 0 0 0 6.6 6.6l2.2-2.2a1 1 0 0 1 1-.25 11.4 11.4 0 0 0 3.6.57 1 1 0 0 1 1 1V20a1 1 0 0 1-1 1A17 17 0 0 1 3 4a1 1 0 0 1 1-1h3.5a1 1 0 0 1 1 1c0 1.25.2 2.45.57 3.57a1 1 0 0 1-.25 1z"/></svg>
        03 9000 4817
      </li>
      <li>
        <svg viewBox="0 0 24 24"><path d="M7 2h10v5H7zM3 8h18v9h-4v5H7v-5H3zm6 8v4h6v-4z"/></svg>
        03 9000 4818
      </li>
      <li>
        <svg viewBox="0 0 24 24"><path d="M2 5h20v14H2zm2 2v.5l8 5 8-5V7zm0 2.8V17h16V9.8l-8 5z"/></svg>
        dan@kestrelphysiostudio.com.au
      </li>
      <li>
        <svg viewBox="0 0 24 24"><path d="M12 2a10 10 0 1 0 0 20 10 10 0 0 0 0-20zm0 2c.9 1.2 1.6 2.9 1.9 5h-3.8c.3-2.1 1-3.8 1.9-5zM4.3 13a8 8 0 0 1 0-2h3.8a19 19 0 0 0 0 2zm.6 2h3.4c.3 1.6.8 3 1.4 4.1A8 8 0 0 1 4.9 15zm3.4-6H4.9a8 8 0 0 1 4.8-4.1C9.1 6 8.6 7.4 8.3 9zM12 20c-.9-1.2-1.6-2.9-1.9-5h3.8c-.3 2.1-1 3.8-1.9 5zm2.1-7H9.9a17 17 0 0 1 0-2h4.2a17 17 0 0 1 0 2zm.2 6.1c.6-1.1 1.1-2.5 1.4-4.1h3.4a8 8 0 0 1-4.8 4.1zM15.9 13a19 19 0 0 0 0-2h3.8a8 8 0 0 1 0 2zm-.2-4c-.3-1.6-.8-3-1.4-4.1A8 8 0 0 1 19.1 9z"/></svg>
        kestrelphysiostudio.com.au
      </li>
      <li>
        <svg viewBox="0 0 24 24"><path d="M12 2a7 7 0 0 0-7 7c0 5 7 13 7 13s7-8 7-13a7 7 0 0 0-7-7zm0 9.5A2.5 2.5 0 1 1 12 6.5a2.5 2.5 0 0 1 0 5z"/></svg>
        12 Linden St, Northfield
      </li>
    </ul>
  </section>

</body>
</html>
```